Web Page for marketing online agency

We are an online marketing agency that is acing the direct response model. We engage with our customers throughout different marketing techniques as research copy-writing, advertisements and content writing. We would need a website design that will have four main aspects: The Vision; stating who we are, The Mission; stating what we do, The Team And It's Values, and a Contact Form. For this design we would want a sharp, clean and smart approach, with illustrated elements or suggestive images. You can use the attached copy, the logo, the USP and the motto. Please integrate them as you see fit while keeping in mind the previous needs and copy. This website is going to be our connection with our possible partners, future colleagues and even our clients. You may submit a design for one page or integrate the 4 different aspects on separate web pages.
Target Market(s)
business partners, future employees, age range 25-60
Industry/Entity Type
Direct Marketing
Number of Pages Required
1 page
Requirements
Must have
- Menu / Header
- 4 Parts or 4 Pages including: vision, mission, team, contact
- Logo
- Motto: Direct Brilliance
- USP: We help people help themselves.
- The copy attached
Nice to have
- Representative illustrated images or elements
Should not have
- A boring design, classical design - WordPress like

```html
<!DOCTYPE html>
<html lang="en">
<head>
<meta charset="utf-8">
<title>NovaKin — Direct Brilliance</title>
<link href="https://fonts.googleapis.com/css2?family=PT+Sans:wght@400;700&family=Roboto+Condensed:wght@400;700&display=swap" rel="stylesheet">
<style>
:root{
  --blue-deep:#1a3ccf;
  --blue:#2a63e6;
  --blue-bright:#3a8ef0;
  --accent:#1c8fd6;
  --ink:#111318;
  --text:#4a4f5a;
  --pale:#cfe0f1;
  --pale-2:#f1f5fb;
  --white:#ffffff;
  --line:#d9dee7;
}
*{box-sizing:border-box;margin:0;padding:0}
html,body{width:1200px;height:2765px;overflow:hidden}
body{position:relative;background:var(--white);font-family:"PT Sans",sans-serif;color:var(--text)}
.abs{position:absolute}
.heading{font-family:"Roboto Condensed",sans-serif;font-weight:700;color:var(--ink)}
.subheading{font-family:"Roboto Condensed",sans-serif;font-weight:700;color:var(--accent);font-size:20px}
.copy{font-size:11px;line-height:20px;color:var(--text)}

/* hero */
.hero-bg{left:0;top:0}
.site-header{left:0;top:0;width:1200px;height:100px}
.logo{display:flex;align-items:center;gap:8px;font-family:"PT Sans",sans-serif;font-weight:700;font-size:38px;color:var(--ink)}
.logo-dot{width:18px;height:18px;border-radius:50%;background:var(--accent)}
.site-header .logo{position:absolute;left:229px;top:34px}
.nav{position:absolute;left:530px;top:32px;display:flex;align-items:center;gap:34px;font-family:"Roboto Condensed",sans-serif;font-size:10px;font-weight:700;color:var(--white);letter-spacing:.3px}
.register{display:flex;align-items:center;gap:6px;background:var(--white);color:var(--blue);border-radius:16px;padding:8px 16px;margin-left:10px}
.hero-title{left:229px;top:222px;font-family:"Roboto Condensed",sans-serif;font-weight:700;font-size:56px;line-height:66px;color:var(--white)}
.hero-sub{left:229px;top:389px;font-family:"Roboto Condensed",sans-serif;font-size:16px;color:var(--white)}
.hero-art{left:802px;top:147px;width:342px;height:452px;border-radius:6px;background:linear-gradient(160deg,#e9b534 0%,#f0f2f5 45%,#3b6fa6 100%)}

/* vision */
.who{right:232px;top:688px;font-size:33px;text-align:right}
.vision-sub{right:232px;top:738px;text-align:right}
.vision-copy{left:330px;width:638px;top:772px;text-align:right}
.values-link{right:232px;top:826px;font-family:"Roboto Condensed",sans-serif;font-size:11px;font-weight:700;color:var(--ink);text-decoration:underline}
.value{top:864px;width:146px;text-align:right}
.value svg{display:block;margin:0 8px 0 auto}
.value h4{font-family:"Roboto Condensed",sans-serif;font-size:13px;color:var(--ink);margin:12px 0 10px}
.value p{font-size:10px;line-height:16px;color:var(--text)}
.dots{left:956px;top:992px;display:flex;gap:3px}
.dots i{width:5px;height:5px;border-radius:50%;background:var(--blue-deep)}
.dots i+i{background:var(--accent)}

/* mission */
.mission-band{left:0;top:1060px;width:1200px;height:590px;background:var(--pale)}
.mission-art{left:175px;top:1198px;width:360px;height:295px;border-radius:10px;background:linear-gradient(180deg,#c3d6ea 0%,#9aa7b6 60%,#d8e4f0 100%)}
.mission-title{left:656px;top:1226px;font-size:32px}
.mission-sub{left:656px;top:1274px}
.mission-copy{left:656px;top:1318px;width:320px}
.btn-outline{left:656px;top:1482px;width:110px;height:32px;border:1.5px solid #9cc7ea;border-radius:16px;background:var(--white);font-family:"Roboto Condensed",sans-serif;font-size:9px;font-weight:700;color:var(--ink);display:flex;align-items:center;justify-content:center}

/* team */
.team-title{left:0;width:1200px;top:1700px;text-align:center;font-size:32px}
.team-sub{left:0;width:1200px;top:1746px;text-align:center}
.team-copy{left:300px;width:600px;top:1786px;text-align:center;font-size:10px;line-height:18px}
.member{top:1844px;width:340px;text-align:center}
.avatar{width:82px;height:82px;border-radius:50%;margin:0 auto 24px;background:linear-gradient(160deg,#d9d9d9,#6b6b6b)}
.member h5{font-family:"PT Sans",sans-serif;font-weight:700;font-size:10px;line-height:16px;color:var(--ink);text-transform:uppercase}
.member p{font-size:10px;margin-top:6px;color:var(--ink)}

/* contact */
.contact-band{left:0;top:2055px;width:1200px;height:378px;background:linear-gradient(90deg,var(--blue-deep) 0%,var(--blue) 50%,var(--blue-bright) 100%)}
.contact-title{left:0;width:1200px;top:2110px;text-align:center;font-size:32px;color:var(--white)}
.contact-copy{left:390px;width:420px;top:2160px;text-align:center;font-size:10px;line-height:18px;color:var(--white)}
.field{height:22px;border-bottom:1px solid rgba(255,255,255,.85);font-family:"Roboto Condensed",sans-serif;font-size:9px;color:var(--white);text-transform:uppercase}
.btn-submit{left:546px;top:2349px;width:108px;height:32px;border-radius:16px;background:var(--white);font-family:"Roboto Condensed",sans-serif;font-size:9px;font-weight:700;color:var(--ink);display:flex;align-items:center;justify-content:center}

/* footer */
.footer{left:0;top:2433px;width:1200px;height:291px;background:var(--pale-2)}
.footer .logo{position:absolute;left:229px;top:78px}
.f-col{top:2583px;font-size:10px;color:var(--ink)}
.f-col h6{font-family:"PT Sans",sans-serif;font-weight:700;font-size:11px;margin-bottom:14px;text-transform:uppercase}
.f-col li{list-style:none;line-height:20px}
.f-col .accent{color:var(--accent);font-weight:700}
.social li{display:flex;align-items:center;gap:6px;line-height:22px}
.social i{width:16px;height:16px;border:1.2px solid var(--ink);border-radius:50%}
.copyright{left:0;top:2724px;width:1200px;height:41px;border-top:1px solid var(--line);display:flex;align-items:center;justify-content:center;font-size:10px;color:var(--ink)}
</style>
</head>
<body>

<svg class="abs hero-bg" width="1200" height="1000" viewBox="0 0 1200 1000" aria-hidden="true">
  <defs>
    <linearGradient id="heroGrad" x1="0" y1="1" x2="1" y2="0">
      <stop offset="0" stop-color="#1a3ccf"/>
      <stop offset="1" stop-color="#2a63e6"/>
    </linearGradient>
  </defs>
  <path d="M0 0 H995 Q1032 276 866 424 L0 885 Z" fill="url(#heroGrad)"/>
  <g fill="none" stroke="#5b86f0" stroke-width="4" opacity=".75">
    <circle cx="63" cy="173" r="10"/><circle cx="478" cy="22" r="9"/><circle cx="173" cy="395" r="14"/>
    <circle cx="410" cy="474" r="15"/><circle cx="335" cy="632" r="9"/><circle cx="37" cy="798" r="9"/>
    <rect x="678" y="130" width="20" height="20" transform="rotate(45 688 140)"/>
    <rect x="196" y="528" width="20" height="20" transform="rotate(45 206 538)"/>
    <rect x="540" y="575" width="16" height="16" transform="rotate(45 548 583)"/>
  </g>
</svg>

<header class="abs site-header">
  <div class="logo">NovaKin<span class="logo-dot"></span></div>
  <nav class="nav">
    <svg width="16" height="14" viewBox="0 0 16 14" aria-label="Home"><path d="M8 0 L16 7 H13 V14 H9.5 V9.5 H6.5 V14 H3 V7 H0 Z" fill="#fff"/></svg>
    <span>VISION</span><span>MISSION</span><span>TEAM</span><span>CONTACT</span>
    <span class="register"><svg width="10" height="10" viewBox="0 0 10 10"><circle cx="5" cy="3" r="2.5" fill="#2a63e6"/><path d="M0 10 Q5 3 10 10 Z" fill="#2a63e6"/></svg>REGISTER</span>
  </nav>
</header>

<h1 class="abs hero-title">We Help People Help<br>Themselves.</h1>
<p class="abs hero-sub">WE ARE SPECIALIZED IN THE SELF-RELIANCE MARKET &amp; TO GROW INDIVIDUALLY</p>
<div class="abs hero-art" role="img" aria-label="Illustration of a person working at a desk with a monitor showing a light bulb idea"></div>

<section>
  <h2 class="abs heading who">WHO WE ARE ?</h2>
  <h3 class="abs subheading vision-sub">Our Vision</h3>
  <p class="abs copy vision-copy">We are a direct response company that creates and sells information products and services that millions of people find interesting and important in their lives.We are specialized in the self reliance market and we serve conservative Americans.</p>
  <span class="abs values-link">OUR VALUES</span>

  <div class="abs value" style="left:232px">
    <svg width="30" height="30" viewBox="0 0 30 30"><path d="M15 3 V26 M6 8 H24 M9 26 H21" stroke="#1c8fd6" stroke-width="2.4" fill="none"/><path d="M2 17 L6 8 L10 17 Z M20 17 L24 8 L28 17 Z" fill="#1c8fd6"/></svg>
    <h4>Fairnes</h4>
    <p>We deliver empowermenthrough products thatcreate fertile short-cuts to solutions....</p>
  </div>
  <div class="abs value" style="left:435px">
    <svg width="30" height="30" viewBox="0 0 30 30"><path d="M15 20 C6 13 9 6 15 10 C21 6 24 13 15 20 Z" fill="#1c8fd6"/><path d="M3 4 V16 L10 26 M27 4 V16 L20 26" stroke="#1c8fd6" stroke-width="2.4" fill="none"/></svg>
    <h4>Caring</h4>
    <p>We deliver empowermenthrough products thatcreate fertile short-cuts to solutions....</p>
  </div>
  <div class="abs value" style="left:623px">
    <svg width="30" height="30" viewBox="0 0 30 30"><path d="M14 3 L24 7 V13 C24 18 19 21 14 22 C9 21 4 18 4 13 V7 Z" fill="#1c8fd6"/><path d="M2 24 H12 L20 27 H28" stroke="#1c8fd6" stroke-width="2.4" fill="none"/></svg>
    <h4>Safety</h4>
    <p>We deliver empowermenthrough products thatcreate fertile short-cuts to solutions....</p>
  </div>
  <div class="abs value" style="left:822px">
    <svg width="30" height="30" viewBox="0 0 30 30"><rect x="9" y="10" width="13" height="18" rx="3" fill="#1c8fd6"/><path d="M11 10 V3 M14.5 10 V2 M18 10 V3 M22 14 L26 9" stroke="#1c8fd6" stroke-width="2.6" stroke-linecap="round"/></svg>
    <h4>Freedom</h4>
    <p>We deliver empowermenthrough products thatcreate fertile short-cuts to solutions....</p>
  </div>
  <div class="abs dots"><i></i><i></i></div>
</section>

<section>
  <div class="abs mission-band"></div>
  <svg class="abs" style="left:0;top:1060px" width="1200" height="590" viewBox="0 0 1200 590" aria-hidden="true">
    <path d="M640 60 Q590 64 588 120 L592 470 Q596 520 660 530 L1200 500 V20 Q1196 10 1180 12 Z" fill="#f6f9fd"/>
    <g fill="none" stroke="#b3cbe6" stroke-width="4">
      <circle cx="68" cy="61" r="14"/><circle cx="483" cy="62" r="14"/><circle cx="860" cy="54" r="9"/>
      <circle cx="218" cy="510" r="12"/><circle cx="698" cy="450" r="9"/>
      <rect x="90" y="205" width="18" height="18" transform="rotate(45 99 214)"/>
      <rect x="48" y="498" width="18" height="18" transform="rotate(45 57 507)"/>
      <rect x="864" y="535" width="18" height="18" transform="rotate(45 873 544)"/>
      <rect x="1152" y="460" width="18" height="18" transform="rotate(45 1161 469)"/>
    </g>
  </svg>
  <div class="abs mission-art" role="img" aria-label="Illustration of a laptop, tablet and phone surrounded by chat and media icons"></div>
  <h2 class="abs heading mission-title">WHAT IS IT THAT WE DO</h2>
  <h3 class="abs subheading mission-sub">Our Mission</h3>
  <p class="abs copy mission-copy">We might not directly save lives, but we try to make a change. We help people help themselves.With our thirst for knowledge and drive for constant improvement, we know we'll find a solution to any challenge.And while doing that, we decided to water our inner seeds and harvest the best of our humanity.We invest time and energy in becoming better in the competition with ourselves.We believe that our better selves of tomorrow will nurture....</p>
  <span class="abs btn-outline">LEARN MORE</span>
</section>

<section>
  <h2 class="abs heading team-title">OUR TEAM</h2>
  <h3 class="abs subheading team-sub">Values</h3>
  <p class="abs copy team-copy">We're a small team of smart, funny hard-working specialists who are pushing to become the #1 company in self reliance. High ambition, radical honesty and a result-oriented mindset are encouraged at NovaKin...</p>
  <div class="abs member" style="left:235px">
    <div class="avatar" role="img" aria-label="Portrait photo of Dorian Vale"></div>
    <h5>Dorian started or was involved in 15 failed businesses<br>before discovering online copywriting.</h5>
    <p>Dorian Vale , CEO NovaKin</p>
  </div>
  <div class="abs member" style="left:617px">
    <div class="avatar" role="img" aria-label="Portrait photo of Marcus Vale" style="background:linear-gradient(160deg,#c9a26d,#2b2b2b)"></div>
    <h5>Since the company's late 2012 start, Marcus grew anetwork<br>of 5000 affiliates, that dominatesniche</h5>
    <p>Marcus Vale , Cofounder &amp; Affiliate Manager NovaKin</p>
  </div>
</section>

<section>
  <div class="abs contact-band"></div>
  <h2 class="abs heading contact-title">KEEP IN TOUCH</h2>
  <p class="abs contact-copy">Lorem Ipsum is simply dummy text of the printing and typesetting industry. Lorem Ipsum has been the industry's standard dummy text</p>
  <div class="abs field" style="left:229px;top:2240px;width:208px">Full Name</div>
  <div class="abs field" style="left:496px;top:2240px;width:206px">E-mail</div>
  <div class="abs field" style="left:761px;top:2240px;width:207px">Website</div>
  <div class="abs field" style="left:229px;top:2289px;width:739px">Message</div>
  <span class="abs btn-submit">SUBMIT</span>
</section>

<footer class="abs footer">
  <div class="logo">NovaKin<span class="logo-dot"></span></div>
</footer>
<div class="abs f-col" style="left:229px;width:220px">
  <h6>Address :</h6>
  <ul>
    <li style="line-height:18px">Lorem Ipsum is simply dummy text of the printing and typesetting industry Lorem...</li>
    <li class="accent" style="margin-top:6px">Email : info@novakin.com</li>
    <li class="accent">Phone : +1 555 010 2233</li>
  </ul>
</div>
<div class="abs f-col" style="left:546px">
  <h6>Navigation</h6>
  <ul><li>Vision</li><li>Mission</li><li>Team</li><li>contact</li></ul>
</div>
<div class="abs f-col" style="left:715px">
  <h6>Quick Links</h6>
  <ul><li>Support</li><li>Help</li><li>Blog</li><li>Privacy Policy</li></ul>
</div>
<div class="abs f-col social" style="left:907px">
  <h6>Follow Us</h6>
  <ul><li><i></i>Newsfeed</li><li><i></i>Microblog</li><li><i></i>Pinboard</li><li><i></i>Searchline</li></ul>
</div>
<div class="abs copyright">© Copyright 2018 NovaKin. All Rights Reserved.</div>

</body>
</html>
```